Corvid Lens Studio Business Card Design

I need a business card designed for a photography business based in Perth, Western Australia called Corvid Lens Studio.

We specialise in wedding, event photography and portrait photography.

The business card must borrow the style of the attached logo.

The hex codes for the colours in the logo are:
#ED1D85 - Pink
#89C23E - Green
#37282F - Black

The name on the card will be:
Name: Tobiah
Phone: 0417395268
Website: www.corvidlensstudio.com.au
Facebook: corvidlensstudio

I am open and happy to accept creative concepts.

Industry/Entity Type

Business

```html
<!DOCTYPE html>
<html lang="en">
<head>
<meta charset="utf-8">
<title>Corvid Lens Studio – Business Card</title>
<link rel="stylesheet" href="https://fonts.googleapis.com/css2?family=Montserrat:wght@300;400;500&display=swap">
<style>
  :root {
    --backdrop: #e7e5e3;
    --card-green: #93c13a;
    --card-white: #f7f7f5;
    --ink-white: #ffffff;
    --ink-dark: #37282f;
    --brand-pink: #ed1d85;
    --card-shadow: 0 18px 40px rgba(40, 30, 35, 0.18), 0 3px 8px rgba(40, 30, 35, 0.12);
  }
  * { box-sizing: border-box; margin: 0; padding: 0; }
  html, body {
    width: 1200px;
    height: 873px;
    overflow: hidden;
    background: var(--backdrop);
    font-family: "Montserrat", Arial, sans-serif;
  }
  .card-set {
    width: 1200px;
    height: 873px;
    display: flex;
    align-items: center;
    justify-content: center;
    gap: 60px;
  }
  .card {
    width: 510px;
    height: 300px;
    border-radius: 4px;
    box-shadow: var(--card-shadow);
    position: relative;
    overflow: hidden;
  }

  /* Front: contact side */
  .card--front {
    background: var(--card-green);
    color: var(--ink-white);
  }
  .studio-name {
    position: absolute;
    left: 40px;
    top: 42px;
    font-weight: 300;
    font-size: 21px;
    letter-spacing: 0.42em;
    text-transform: uppercase;
    white-space: nowrap;
  }
  .studio-rule {
    position: absolute;
    left: 180px;
    top: 96px;
    width: 260px;
    height: 1.5px;
    background: var(--ink-white);
  }
  .contact {
    position: absolute;
    left: 40px;
    bottom: 40px;
    list-style: none;
    font-weight: 400;
    font-size: 10.5px;
    letter-spacing: 0.16em;
    text-transform: uppercase;
    line-height: 1.75;
  }
  .contact__name {
    font-weight: 500;
    font-size: 13px;
    letter-spacing: 0.22em;
    color: var(--ink-dark);
    margin-bottom: 2px;
  }
  .contact__phone { margin-bottom: 10px; }

  /* Back: brand side */
  .card--back {
    background: var(--card-white);
    display: flex;
    align-items: center;
    justify-content: center;
    gap: 14px;
  }
  .brand-dot {
    width: 22px;
    height: 22px;
    border-radius: 50%;
    background: var(--brand-pink);
    flex: none;
  }
  .brand-name {
    font-weight: 400;
    font-size: 22px;
    letter-spacing: 0.12em;
    color: var(--ink-dark);
    white-space: nowrap;
  }
</style>
</head>
<body>
  <main class="card-set">
    <section class="card card--front" aria-label="Business card front">
      <h1 class="studio-name">Corvid Lens Studio</h1>
      <div class="studio-rule"></div>
      <ul class="contact">
        <li class="contact__name">Tobiah</li>
        <li class="contact__phone">04 1739 5268</li>
        <li class="contact__web">www.corvidlensstudio.com.au</li>
        <li class="contact__social">@corvidlensstudio</li>
      </ul>
    </section>

    <section class="card card--back" aria-label="Business card back">
      <span class="brand-dot"></span>
      <span class="brand-name">Corvid Lens Studio</span>
    </section>
  </main>
</body>
</html>
```